ALL TEXT GRAPHICS TM May 2025 for Instagram

We are looking for a series of social media graphics for Instagram (new size: 4:5 (1080 x 1350 pixels) ratio that are ALL TEXT. We want the following quotes below on each graphic; one quote per graphic. AND, In very small letters at the bottom of each graphic, add @TovaMarshOnline
The look and feel of these graphics should be complimentary to the color palette attached below; but keep them simple. But the design is up to you; at the end of this document, I provided various samples of all text graphics that I like as examples.
Target Market(s)
women looking to lose weight
Look and feel

```html
<!DOCTYPE html>
<html lang="en">
<head>
<meta charset="utf-8">
<title>TM All Text Graphics – May 2025</title>
<link rel="stylesheet" href="https://fonts.googleapis.com/css2?family=Poppins:wght@300;400;600;800&display=swap">
<style>
  :root {
    --canvas: #e1e1e1;
    --mauve: #876a78;
    --wine: #660033;
    --blush: #d1b5b5;
    --plum: #935572;
    --coral: #f89ba4;
    --berry: #a21c5c;
    --sand: #d1c7b4;
    --lilac: #aa88ae;
    --silver: #cdcccd;
    --raspberry: #990a4d;
    --pink-light: #ffc6e4;
    --pink-soft: #ff9fd0;
    --magenta: #d6006e;
    --white: #ffffff;
  }
  * { box-sizing: border-box; margin: 0; padding: 0; }
  html, body { width: 1200px; height: 800px; overflow: hidden; }
  body {
    background: var(--canvas);
    font-family: "Poppins", sans-serif;
    position: relative;
  }
  .post {
    position: absolute;
    width: 207px;
    height: 258px;
    padding: 18px 18px 0;
    color: var(--accent);
  }
  .col-1 { left: 55px; }  .col-2 { left: 278px; } .col-3 { left: 500px; }
  .col-4 { left: 719px; } .col-5 { left: 939px; }
  .row-1 { top: 135px; }  .row-2 { top: 407px; }

  .chevron { display: block; width: 11px; height: 12px; margin-top: 3px; }
  .headline {
    margin-top: 20px;
    font-weight: 800;
    font-size: 17px;
    line-height: 18.3px;
    letter-spacing: -0.2px;
    color: var(--head);
  }
  .body-copy {
    margin-top: 8px;
    font-weight: 300;
    font-size: 16.5px;
    line-height: 18.3px;
    color: var(--copy);
  }
  .body-copy strong { font-weight: 600; }
  .kicker {
    margin-top: 11px;
    font-weight: 800;
    font-size: 17px;
    line-height: 18.3px;
    letter-spacing: -0.2px;
    color: var(--head);
  }
  .footer {
    position: absolute;
    left: 18px; right: 18px; top: 230px;
    display: flex; align-items: center; gap: 4px;
  }
  .footer.handle-right { flex-direction: row; }
  .footer.handle-left { flex-direction: row-reverse; }
  .footer .rule { flex: 1; height: 0.5px; background: var(--accent); opacity: 0.7; }
  .footer .handle {
    font-size: 5.6px; font-weight: 600; letter-spacing: 0.1px;
    text-transform: uppercase; color: var(--handle, var(--head));
  }

  .post--mauve     { background: var(--mauve);     --head: var(--pink-light); --copy: var(--pink-light); --accent: var(--pink-light); }
  .post--wine      { background: var(--wine);      --head: var(--pink-soft);  --copy: var(--pink-soft);  --accent: var(--pink-soft); }
  .post--blush     { background: var(--blush);     --head: var(--magenta);    --copy: var(--magenta);    --accent: var(--magenta); }
  .post--plum      { background: var(--plum);      --head: var(--white);      --copy: var(--white);      --accent: var(--pink-light); }
  .post--coral     { background: var(--coral);     --head: var(--magenta);    --copy: var(--magenta);    --accent: var(--magenta); }
  .post--berry     { background: var(--berry);     --head: var(--pink-light); --copy: var(--pink-light); --accent: var(--pink-light); }
  .post--sand      { background: var(--sand);      --head: var(--magenta);    --copy: var(--magenta);    --accent: var(--magenta); }
  .post--lilac     { background: var(--lilac);     --head: var(--pink-light); --copy: var(--pink-light); --accent: var(--pink-light); }
  .post--silver    { background: var(--silver);    --head: var(--magenta);    --copy: var(--magenta);    --accent: var(--magenta); }
  .post--raspberry { background: var(--raspberry); --head: var(--white);      --copy: var(--white);      --accent: var(--pink-light); }
  .post--berry .body-copy strong { color: var(--white); font-weight: 800; }
  .post--coral .body-copy strong,
  .post--blush .body-copy strong { font-weight: 800; }
  .post--wine .body-copy { color: #e9a3c4; }
  .post--mauve .handle, .post--berry .handle, .post--raspberry .handle, .post--plum .handle, .post--lilac .handle { --handle: var(--white); }
  .headline.gap-lg { margin-top: 20px; }
</style>
</head>
<body>

<!-- Row 1 -->
<article class="post post--mauve col-1 row-1">
  <svg class="chevron" viewBox="0 0 11 12" fill="none" stroke="currentColor" stroke-width="1.6"><path d="M1 1l4 5-4 5M6 1l4 5-4 5"/></svg>
  <h2 class="headline">Tired. Moody.<br>Stubborn<br>Belly Fat.</h2>
  <p class="body-copy">Your hormones<br>are screaming<br>for help!</p>
  <p class="kicker">Let’s fix that.</p>
  <div class="footer handle-right"><span class="rule"></span><span class="handle">@TovaMarshOnline</span></div>
</article>

<article class="post post--wine col-2 row-1">
  <svg class="chevron" viewBox="0 0 11 12" fill="none" stroke="currentColor" stroke-width="1.6"><path d="M1 1l4 5-4 5M6 1l4 5-4 5"/></svg>
  <h2 class="headline">That stubborn<br>weight?</h2>
  <p class="body-copy">It’s not your fault.<br>Your hormones<br>are to blame and<br>you’re not alone;</p>
  <p class="kicker">But there is a fix.</p>
  <div class="footer handle-right"><span class="rule"></span><span class="handle">@TovaMarshOnline</span></div>
</article>

<article class="post post--blush col-3 row-1">
  <svg class="chevron" viewBox="0 0 11 12" fill="none" stroke="currentColor" stroke-width="1.6"><path d="M1 1l4 5-4 5M6 1l4 5-4 5"/></svg>
  <h2 class="headline">Your belly<br>isn’t fat…<br>it’s hormonal.</h2>
  <p class="body-copy">And here’s how to<br>fix it.&nbsp; Comment<br><strong>HORMONES</strong> if<br>nothing is working.</p>
  <div class="footer handle-left"><span class="rule"></span><span class="handle">@TovaMarshOnline</span></div>
</article>

<article class="post post--plum col-4 row-1">
  <svg class="chevron" viewBox="0 0 11 12" fill="none" stroke="currentColor" stroke-width="1.6"><path d="M1 1l4 5-4 5M6 1l4 5-4 5"/></svg>
  <h2 class="headline">The stubborn<br>belly fat after 40?</h2>
  <p class="body-copy">It’s not about<br>calories; it’s about<br>your hormones.</p>
  <p class="kicker" style="margin-top:18px">Here is the fix!</p>
  <div class="footer handle-left"><span class="rule"></span><span class="handle">@TovaMarshOnline</span></div>
</article>

<article class="post post--coral col-5 row-1">
  <svg class="chevron" viewBox="0 0 11 12" fill="none" stroke="currentColor" stroke-width="1.6"><path d="M1 1l4 5-4 5M6 1l4 5-4 5"/></svg>
  <h2 class="headline">Flat tummy in<br>your 40s?</h2>
  <p class="body-copy">It’s still possible!</p>
  <p class="body-copy" style="margin-top:11px">Comment <strong>BYE<br>BELLY</strong> to get the<br>10 secrets to a<br>flatter tummy</p>
  <div class="footer handle-left"><span class="rule"></span><span class="handle">@TovaMarshOnline</span></div>
</article>

<!-- Row 2 -->
<article class="post post--berry col-1 row-2">
  <svg class="chevron" viewBox="0 0 11 12" fill="none" stroke="currentColor" stroke-width="1.6"><path d="M1 1l4 5-4 5M6 1l4 5-4 5"/></svg>
  <h2 class="headline" style="margin-top:26px">This is the secret<br>women over 40</h2>
  <p class="body-copy" style="margin-top:0">are using to get<br>snatched; without<br>starving.</p>
  <p class="body-copy" style="margin-top:11px">Comment<br><strong>SKINNY</strong> to get the<br>exact plan.</p>
  <div class="footer handle-right"><span class="rule"></span><span class="handle">@TovaMarshOnline</span></div>
</article>

<article class="post post--sand col-2 row-2">
  <svg class="chevron" viewBox="0 0 11 12" fill="none" stroke="currentColor" stroke-width="1.6"><path d="M1 1l4 5-4 5M6 1l4 5-4 5"/></svg>
  <h2 class="headline" style="margin-top:22px">Bloating.<br>Muffin top.<br>Puffy waistline.</h2>
  <p class="body-copy">Your body’s<br>screaming for a<br>different kind of fix.</p>
  <p class="kicker" style="margin-top:13px">Here it is</p>
  <div class="footer handle-left"><span class="rule"></span><span class="handle">@TovaMarshOnline</span></div>
</article>

<article class="post post--lilac col-3 row-2">
  <svg class="chevron" viewBox="0 0 11 12" fill="none" stroke="currentColor" stroke-width="1.6"><path d="M1 1l4 5-4 5M6 1l4 5-4 5"/></svg>
  <h2 class="headline" style="margin-top:26px">What worked in<br>your 30s won’t<br>work now.</h2>
  <p class="body-copy" style="margin-top:20px">Here’s what<br>actually does.<br>Drop 30 Pounds in<br>3 Months</p>
  <div class="footer handle-left"><span class="rule"></span><span class="handle">@TovaMarshOnline</span></div>
</article>

<article class="post post--silver col-4 row-2">
  <svg class="chevron" viewBox="0 0 11 12" fill="none" stroke="currentColor" stroke-width="1.6"><path d="M1 1l4 5-4 5M6 1l4 5-4 5"/></svg>
  <h2 class="headline" style="margin-top:26px">You’re doing all<br>the “right”<br>things, but your<br>belly won’t go<br>down?</h2>
  <p class="body-copy" style="margin-top:10px">Here’s what you<br>haven’t tried.</p>
  <div class="footer handle-left"><span class="rule"></span><span class="handle">@TovaMarshOnline</span></div>
</article>

<article class="post post--raspberry col-5 row-2">
  <svg class="chevron" viewBox="0 0 11 12" fill="none" stroke="currentColor" stroke-width="1.6"><path d="M1 1l4 5-4 5M6 1l4 5-4 5"/></svg>
  <h2 class="headline" style="margin-top:26px">This 90-day plan<br>helped women<br>over 40</h2>
  <p class="body-copy" style="margin-top:14px">slim down, get a<br>tiny waist and feel<br>sexy again.</p>
  <p class="kicker">You’re next.</p>
  <div class="footer handle-right"><span class="rule"></span><span class="handle">@TovaMarshOnline</span></div>
</article>

</body>
</html>
```